New Lead input page design

Attached is our concept of a new lead input screen for the back-end of our website which is a tool for a loan agent (2 page PDF attached)

1. This is the first of many other data input screen projects for our website, so the designer that ends up with us will have quite a bit of add on new projects.

2. HERE IS THE LINK WITH THE SAMPLE OF ALL THE CURRENT CONTROLS:
http://apps.brimtally.com/controlWidgets.html

3. The colors and hues of: either GREEN & GREYS or BLUE & GREYS.

4. I think some gradients and shadows adds depth and sophistication. Basically trying to get away from old school flat, one dimensional data screen inputs and add some design flare to it.

5. Upon completion we will need the HTML of the design etc and we will code the input fields directly.

6. See attached files for the entire input screen. Please also add the data input space (see sample) to your design.

Thank you

Reason: We are extending the deadline to give us time to ask current designs to complete slight revisions

Reason: Finalizing the selection for one last variation detailed to current designers

```html
<!DOCTYPE html>
<html lang="en">
<head>
<meta charset="utf-8">
<title>New Lead Input</title>
<link href="https://fonts.googleapis.com/css2?family=Arimo:wght@400;700&display=swap" rel="stylesheet">
<style>
:root{
  --blue:#3a86c8;
  --label:#1f5fae;
  --value:#4a4a4a;
  --alert:#e0261f;
  --grey:#8a8a8a;
  --band:#f1f1f1;
}
*{margin:0;padding:0;box-sizing:border-box}
html,body{width:961px;height:1200px;overflow:hidden;background:#fff;font-family:"Arimo",Arial,sans-serif}
.page{position:relative;width:961px;height:1200px}
.tabs{position:absolute;left:0;top:0;width:961px;height:62px;background:linear-gradient(#fff 85%,#eee);border-bottom:1px solid #e4e4e4}
.tab{position:absolute;top:0;height:62px;display:flex;align-items:center;gap:5px;font-size:9.5px;color:#555}
.tab svg{width:14px;height:14px}
.tab.active{left:138px;width:110px;background:linear-gradient(#3f8dd0,#2f78bb);color:#fff;justify-content:center}
.divider{position:absolute;top:10px;width:1px;height:42px;background:#e6e6e6}
.band{position:absolute;left:138px;width:685px;height:18px;background:linear-gradient(var(--band),#fff)}
.ball{position:absolute;left:155px;width:86px;height:86px;border-radius:50%;display:flex;align-items:center;justify-content:center;text-align:center;color:#fff;font-size:12.5px;line-height:17px;box-shadow:0 3px 5px rgba(0,0,0,.35),inset 0 -6px 12px rgba(0,0,0,.25)}
.ball::before{content:"";position:absolute;left:12px;top:8px;width:52px;height:30px;border-radius:50%;background:linear-gradient(rgba(255,255,255,.55),rgba(255,255,255,0))}
.ball span{position:relative}
.clients{background:radial-gradient(circle at 40% 35%,#8a92cf,#4d569c 70%,#3a4280)}
.existing{background:radial-gradient(circle at 40% 35%,#5fd39b,#21995f 70%,#17784a)}
.newloan{background:radial-gradient(circle at 40% 35%,#6fe1ea,#22aebd 70%,#178895)}
.contact{background:radial-gradient(circle at 40% 35%,#ffd266,#f3a012 70%,#d2830a)}
.credit{background:radial-gradient(circle at 40% 35%,#ff7468,#db201b 70%,#b21411)}
.property{background:radial-gradient(circle at 40% 35%,#ea86f3,#bb34cb 70%,#9320a2)}
.income{background:radial-gradient(circle at 40% 35%,#8a4ac4,#4a1480 70%,#33095c)}
.col{position:absolute;font-size:9.2px}
.col div{height:20.8px;line-height:20.8px;white-space:nowrap}
.col .multi{line-height:14.4px;padding-top:3.2px;height:auto;min-height:20.8px}
.col .multi.tall{min-height:41.6px}
.lab{color:var(--label)}
.val{color:var(--value)}
.red{color:var(--alert)}
.copy{display:inline-block;vertical-align:middle;margin-left:14px;width:15px;height:15px}
.footer{position:absolute;left:0;top:1170px;width:961px;height:30px;background:var(--blue);color:#fff;font-size:8px;display:flex;align-items:center;justify-content:center}
.footer .code{position:absolute;right:56px;font-size:9px}
</style>
</head>
<body>
<div class="page">
  <nav class="tabs">
    <div class="tab active"><svg viewBox="0 0 14 14" fill="none" stroke="#fff" stroke-width="1"><rect x="1" y="1" width="10" height="12"/><path d="M3 4h6M3 7h6M3 10h4"/><circle cx="11" cy="11" r="2.5" fill="#fff"/></svg>Lead Category</div>
    <div class="tab" style="left:270px"><svg viewBox="0 0 14 14" fill="none" stroke="#777"><rect x="1" y="2" width="8" height="10"/><rect x="5" y="4" width="8" height="9" fill="#fff"/><path d="M7 7h4M7 9h4"/></svg>Sticky Note</div>
    <div class="divider" style="left:360px"></div>
    <div class="tab" style="left:389px"><svg viewBox="0 0 14 14" fill="#777"><path d="M5 1h2v7l4 1-1 5H5L2 9l1-1 2 2z"/></svg>Snap Shot</div>
    <div class="divider" style="left:477px"></div>
    <div class="tab" style="left:507px"><svg viewBox="0 0 14 14" fill="none" stroke="#777"><circle cx="7" cy="8" r="5"/><path d="M7 5v3l2 1M2 2l2 2M12 2l-2 2"/></svg>Alerts</div>
    <div class="divider" style="left:582px"></div>
    <div class="tab" style="left:620px"><svg viewBox="0 0 14 14" fill="none" stroke="#777"><rect x="2" y="1" width="10" height="12"/><path d="M4 4h6M4 7h6M4 10h6"/></svg>Lead Notes</div>
    <div class="divider" style="left:711px"></div>
    <div class="tab" style="left:742px"><svg viewBox="0 0 14 14" fill="none" stroke="#777"><rect x="1" y="2" width="12" height="11"/><path d="M1 5h12M4 8h1M7 8h1M10 8h1M4 11h1M7 11h1"/></svg>Calendar</div>
  </nav>

  <!-- Clients -->
  <div class="ball clients" style="top:94px"><span>Clients</span></div>
  <div class="col lab" style="left:286px;top:95px"><div>Borrower :</div><div>Application :</div><div>Lead Stat :</div><div>Demo Stat :</div></div>
  <div class="col val" style="left:390px;top:95px"><div>Daniel Marsh</div><div>Joint</div><div class="red">3</div><div class="red">4</div></div>
  <div class="col lab" style="left:526px;top:95px"><div>Co-Borrower :</div><div>Relationship :</div><div>Add borrowers :</div></div>
  <div class="col val" style="left:630px;top:95px"><div>Ellen Marsh</div><div>Husband &amp; Wife</div><div>N/A</div></div>
  <div class="band" style="top:206px"></div>

  <!-- Existing Loan -->
  <div class="ball existing" style="top:238px"><span>Existing<br>Loan</span></div>
  <div class="col lab" style="left:286px;top:239px"><div>Current Amount :</div><div>Current Loan :</div><div>Apprx. Last Refi :</div><div>Add more Loans :</div></div>
  <div class="col val" style="left:390px;top:239px"><div>$335,758</div><div>30 year fix – 5.5%</div><div>4 years ago</div><div>$59,000 - Heloc</div></div>
  <div class="col lab" style="left:526px;top:239px"><div>How many loans :</div><div>Current P &amp; I :</div><div>Tax &amp; Insurance :</div><div>Total Payment :</div></div>
  <div class="col val" style="left:630px;top:239px"><div>2 <span class="red">Pay off both?</span> Yes</div><div>$2,200</div><div>$450</div><div>$2,650</div></div>
  <div class="band" style="top:350px"></div>

  <!-- New Loan -->
  <div class="ball newloan" style="top:375px"><span>New<br>Loan</span></div>
  <div class="col lab" style="left:286px;top:376px"><div>New Amount :</div><div>New Loan :</div><div>Quoted Rate :</div></div>
  <div class="col val" style="left:390px;top:376px"><div>$336,000</div><div>30 year fix - <span class="red">"select"</span></div><div>5%</div></div>
  <div class="col lab" style="left:526px;top:376px"><div>New Loan Purpose :</div><div>Closing Costs :</div><div>Lender Credit :</div></div>
  <div class="col val" style="left:630px;top:376px"><div>Rate &amp; Term</div><div>$450</div><div>$450</div></div>
  <div class="band" style="top:488px"></div>

  <!-- Contact -->
  <div class="ball contact" style="top:519px"><span>Contact</span></div>
  <div class="col lab" style="left:286px;top:520px"><div>Main Phone :</div><div>Email :</div><div>Address :</div></div>
  <div class="col val" style="left:390px;top:520px"><div>555-010-0199</div><div>daniel@mailbox.test</div><div class="multi">412 Harbor Lane<br>Bayview CA 90000</div></div>
  <div class="col lab" style="left:526px;top:520px"><div>Main Phone :</div><div>Email :</div><div>Address :</div></div>
  <div class="col val" style="left:630px;top:520px"><div>555-010-0199</div><div>ellen@mailbox.test</div><div class="multi">412 Harbor Lane<br>Bayview CA 90000</div></div>
  <div class="band" style="top:632px"></div>

  <!-- Credit -->
  <div class="ball credit" style="top:667px"><span>Credit</span></div>
  <div class="col lab" style="left:286px;top:668px"><div>DOB :</div><div>Daniel's Social :</div><div>Credit Score :</div><div>Credit Pull Date :</div><div>DTI :</div></div>
  <div class="col val" style="left:390px;top:668px"><div>02/22/1975</div><div>000-00-0001</div><div>700 &nbsp; 688 &nbsp; 744<svg class="copy" viewBox="0 0 15 15" fill="#fff" stroke="#e0261f" stroke-width="1.2"><rect x="1" y="1" width="8" height="11"/><rect x="5" y="4" width="8" height="10"/><path d="M7 7h4M7 9.5h4M7 12h4"/></svg></div><div>04/28/14</div><div>44% - 32%</div></div>
  <div class="col lab" style="left:526px;top:668px"><div>DOB :</div><div>Ellen's Social :</div><div>Credit Score :</div><div>Credit Age :</div><div>Credit Impression :</div></div>
  <div class="col val" style="left:630px;top:668px"><div>01/25/1973</div><div>000-00-0002</div><div>712 &nbsp;694 &nbsp;708<svg class="copy" style="margin-left:8px" viewBox="0 0 15 15" fill="#fff" stroke="#e0261f" stroke-width="1.2"><rect x="1" y="1" width="8" height="11"/><rect x="5" y="4" width="8" height="10"/><path d="M7 7h4M7 9.5h4M7 12h4"/></svg></div><div>2 Days</div><div>Excellent</div></div>
  <div class="band" style="top:780px"></div>

  <!-- Property -->
  <div class="ball property" style="top:811px"><span>Property</span></div>
  <div class="col lab" style="left:286px;top:812px"><div style="height:41.6px">Address :</div><div>Property Type :</div><div>Residency :</div><div>Year Built :</div></div>
  <div class="col val" style="left:390px;top:812px"><div class="multi tall">412 Harbor Lane<br>Bayview CA 90000</div><div>SFR</div><div>Primary</div><div>1981</div></div>
  <div class="col lab" style="left:526px;top:812px"><div>Subject Property :</div><div>Number of Properties :</div><div>Special Upgrades :</div><div>Approximate Value :</div><div>Appraised Value :</div></div>
  <div class="col val" style="left:630px;top:812px"><div>Yes - 1 of 3</div><div>3 &nbsp;&nbsp; <span class="red">- Add More</span></div><div>Added a room &amp; roof</div><div>$445,000</div><div>$405,000</div></div>
  <div class="band" style="top:934px"></div>

  <!-- Income -->
  <div class="ball income" style="top:955px"><span>Income</span></div>
  <div class="col lab" style="left:286px;top:956px"><div>Income Source :</div><div>Address :</div><div>Work phone :</div><div>Position :</div><div>Length :</div><div>Term :</div><div>Income :</div><div>Other income :</div></div>
  <div class="col val" style="left:390px;top:956px"><div>Northwind Labs</div><div>88 Cedar way</div><div>555-010-0142</div><div>Admin</div><div>2 years</div><div>3 years</div><div>$3,000</div><div>$ 1,500</div></div>
  <div class="col lab" style="left:526px;top:956px"><div>Income Source :</div><div>Address :</div><div>Work phone :</div><div>Position :</div><div>Length :</div><div>Term :</div><div>Income :</div><div>Other income :</div></div>
  <div class="col val" style="left:630px;top:956px"><div>Northwind Labs</div><div>88 Cedar way</div><div>555-010-0142</div><div class="red">Manager</div><div>4 years</div><div>2 years</div><div>$4,500</div><div>$ 1,900</div></div>

  <footer class="footer">© 2014 Company name. All rights reserved.<span class="code">C8</span></footer>
</div>
</body>
</html>
```